Business Card & Stationery Design for a General Contracting Company
Brenwick Contracting Limited
Tolvane Perdo
Managing Director
No 7 Marlowe Crescent, Elmsby
brenwickcontracting@quillpost.net
The Company is involved in supply and transport of aggregate materials and heavy equipment rental at present. Furthermore we recently had a project for the logo design of our Company on this website and we would like to incorporate this logo into our stationery designs and business cards. Please see the links below; Our design project; http://orders.markcraftstudio.net/contests/logo-for-a-general-contracting-company The logo chosen; http://orders.markcraftstudio.net/drafts/display/contest/512093/draft/e7d4b58213690ab1c5f93d478ee2bb718204617

```html
<!DOCTYPE html>
<html lang="en">
<head>
<meta charset="utf-8">
<title>Brenwick Contracting Limited – Business Card</title>
<link href="https://fonts.googleapis.com/css2?family=Roboto:wght@400;700&family=Roboto+Condensed:wght@700&display=swap" rel="stylesheet">
<style>
  :root {
    --backdrop: #e9e6e1;
    --card-white: #ffffff;
    --brand-blue: #1f5fa8;
    --brand-blue-dark: #184c89;
    --brand-red: #c4161c;
    --text-light: #ffffff;
    --text-dark: #1f5fa8;
  }
  html, body {
    margin: 0;
    padding: 0;
    width: 1200px;
    height: 902px;
    overflow: hidden;
    background: var(--backdrop);
    font-family: "Roboto", Arial, sans-serif;
  }
  .canvas {
    position: relative;
    width: 1200px;
    height: 902px;
  }
  .business-card {
    position: absolute;
    left: 150px;
    top: 194px;
    width: 900px;
    height: 514px;
    background: var(--card-white);
    box-shadow: 0 14px 36px rgba(0,0,0,0.25);
    overflow: hidden;
  }
  .card-shapes {
    position: absolute;
    inset: 0;
  }
  .brand-lockup {
    position: absolute;
    left: 56px;
    top: 52px;
    display: flex;
    align-items: center;
    gap: 18px;
  }
  .brand-mark {
    width: 64px;
    height: 64px;
    border-radius: 50%;
    background: var(--brand-red);
  }
  .brand-name {
    font-family: "Roboto Condensed", "Arial Narrow", sans-serif;
    font-weight: 700;
    color: var(--text-dark);
    font-size: 34px;
    line-height: 1.05;
    text-transform: uppercase;
    letter-spacing: 0.5px;
  }
  .cardholder {
    position: absolute;
    right: 60px;
    top: 200px;
    text-align: right;
    color: var(--text-light);
  }
  .cardholder-name {
    font-size: 24px;
    font-weight: 700;
    margin: 0;
  }
  .cardholder-title {
    font-size: 18px;
    margin: 4px 0 0;
  }
  .website-tab {
    position: absolute;
    right: 60px;
    top: 342px;
    color: var(--text-light);
    font-size: 17px;
  }
  .contact-list {
    position: absolute;
    left: 40px;
    top: 298px;
    margin: 0;
    padding: 0;
    list-style: none;
    color: var(--text-light);
    font-size: 15px;
  }
  .contact-item {
    display: flex;
    align-items: center;
    gap: 10px;
    height: 24px;
  }
  .contact-icon {
    width: 16px;
    height: 16px;
    flex: none;
  }
</style>
</head>
<body>
<main class="canvas">
  <section class="business-card" aria-label="Business card front">
    <svg class="card-shapes" width="900" height="514" viewBox="0 0 900 514" aria-hidden="true">
      <rect x="0" y="168" width="900" height="346" fill="var(--brand-blue)"/>
      <polygon points="708,168 730,148 752,168" fill="var(--brand-blue)"/>
      <path d="M0,488 L470,488 C520,488 520,330 580,330 L900,330 L900,378 L610,378 C560,378 560,514 500,514 L0,514 Z" fill="var(--brand-red)"/>
    </svg>

    <div class="brand-lockup">
      <div class="brand-mark"></div>
      <div class="brand-name">Brenwick Contracting<br>Limited</div>
    </div>

    <div class="cardholder">
      <p class="cardholder-name">Tolvane Perdo</p>
      <p class="cardholder-title">Managing Director</p>
    </div>

    <div class="website-tab">www.brenwickbuild.net</div>

    <ul class="contact-list">
      <li class="contact-item">
        <svg class="contact-icon" viewBox="0 0 16 16"><circle cx="8" cy="8" r="8" fill="#fff"/><path d="M8 3.5a3 3 0 0 0-3 3c0 2.2 3 6 3 6s3-3.8 3-6a3 3 0 0 0-3-3zm0 4.2a1.2 1.2 0 1 1 0-2.4 1.2 1.2 0 0 1 0 2.4z" fill="var(--brand-blue)"/></svg>
        No 7 Marlowe Crescent, Elmsby
      </li>
      <li class="contact-item">
        <svg class="contact-icon" viewBox="0 0 16 16"><circle cx="8" cy="8" r="8" fill="#fff"/><path d="M5.2 4l1.6-.3 1 2.1-1 .8a5 5 0 0 0 2.6 2.6l.8-1 2.1 1-.3 1.6c-4 .5-7.3-2.8-6.8-6.8z" fill="var(--brand-blue)"/></svg>
        555-0148
      </li>
      <li class="contact-item">
        <svg class="contact-icon" viewBox="0 0 16 16"><circle cx="8" cy="8" r="8" fill="#fff"/><rect x="5.5" y="3.5" width="5" height="9" rx="1" fill="var(--brand-blue)"/><rect x="6.3" y="4.6" width="3.4" height="5.6" fill="#fff"/></svg>
        555-0172
      </li>
      <li class="contact-item">
        <svg class="contact-icon" viewBox="0 0 16 16"><circle cx="8" cy="8" r="8" fill="#fff"/><rect x="4" y="6" width="8" height="5.5" rx="1" fill="var(--brand-blue)"/><rect x="5.5" y="3.8" width="5" height="2.6" fill="var(--brand-blue)"/></svg>
        555-0193
      </li>
      <li class="contact-item">
        <svg class="contact-icon" viewBox="0 0 16 16"><circle cx="8" cy="8" r="8" fill="#fff"/><rect x="3.8" y="5" width="8.4" height="6" rx="0.8" fill="var(--brand-blue)"/><path d="M4.2 5.4L8 8.4l3.8-3" fill="none" stroke="#fff" stroke-width="0.9"/></svg>
        brenwickcontracting@quillpost.net
      </li>
      <li class="contact-item">
        <svg class="contact-icon" viewBox="0 0 16 16"><circle cx="8" cy="8" r="8" fill="#fff"/><circle cx="8" cy="8" r="4.3" fill="none" stroke="var(--brand-blue)" stroke-width="1.1"/><ellipse cx="8" cy="8" rx="1.8" ry="4.3" fill="none" stroke="var(--brand-blue)" stroke-width="0.9"/><line x1="3.7" y1="8" x2="12.3" y2="8" stroke="var(--brand-blue)" stroke-width="0.9"/></svg>
        www.brenwickbuild.net
      </li>
    </ul>
  </section>
</main>
</body>
</html>
```